Ridgeline Outfitters Business Cards

Recently had a logo done with Artfolio and now looking for a business card to go along with it.

Target Market(s)

Ridgeline Outfitters is a weapons dealer. My market will be primarily men, hunting, shooting type.

Industry/Entity Type

Business

Contact Information for Business Card

I selected double sided, but this is not required, single or double is going to be fine. I picture the logo on one side, or perhaps just the circle which contains "RO" with the remaining info on the other side.

Font styles to use
Sans Serif

Requirements
Must have
• My name: Milo Brandt
• Title: Owner
• tel: 612-555-0187
• web: www.ridgelineoutfittersmn.example
Nice to have
• I like the concept of a black business card. I would like to keep the colors monotone, black, grey, white or red. Red is acceptable because it is in the logo. I have also seen cards that are matte black with shiny black as well, perhaps for the logo (or circle RO) part of the logo.
• I will upload a couple of the logos for use, and also an example I just found of the black on black. and some others that have a nice contrast.
Should not have
• lots of colors are not wanted.

```html
<!DOCTYPE html>
<html lang="en">
<head>
<meta charset="utf-8">
<title>Ridgeline Outfitters Business Cards</title>
<link rel="stylesheet" href="https://fonts.googleapis.com/css2?family=Lexend:wght@400;600;800&display=swap">
<style>
  :root {
    --backdrop: #8c8c8c;
    --card-black: #0b0c0f;
    --card-sheen: #1a1b20;
    --brand-red: #ff1414;
    --steel-grey: #5d6163;
    --shadow-black: #141414;
  }
  * { margin: 0; padding: 0; box-sizing: border-box; }
  html, body { width: 1200px; height: 1200px; overflow: hidden; }
  body {
    background: var(--backdrop);
    font-family: "Lexend", sans-serif;
    position: relative;
  }
  .card {
    position: absolute;
    left: 150px;
    width: 900px;
    height: 514px;
    overflow: hidden;
    background: radial-gradient(ellipse at 40% 30%, var(--card-sheen), var(--card-black) 75%);
    box-shadow: 0 10px 28px rgba(0,0,0,0.45);
    color: var(--brand-red);
  }
  .card--info { top: 60px; }
  .card--brand { top: 626px; }

  .wordmark {
    font-weight: 800;
    text-transform: uppercase;
    letter-spacing: 1px;
    color: var(--brand-red);
    white-space: nowrap;
  }
  .card--info .wordmark {
    position: absolute;
    top: 96px;
    left: 0; right: 0;
    text-align: center;
    font-size: 50px;
  }
  .holder {
    position: absolute;
    left: 0; right: 0;
    text-align: center;
  }
  .holder__name { top: 212px; font-size: 34px; font-weight: 600; }
  .holder__title { top: 258px; font-size: 28px; font-weight: 600; }
  .name-first { color: var(--shadow-black); }

  .contact {
    position: absolute;
    left: 0; right: 0;
    text-align: center;
    font-weight: 600;
  }
  .contact__phone { top: 356px; font-size: 32px; }
  .contact__phone svg { vertical-align: -3px; margin-right: 10px; }
  .contact__web { top: 408px; font-size: 28px; }

  .card--brand .holder__name {
    position: absolute;
    top: 120px;
    right: 70px;
    text-align: right;
    font-size: 34px;
    font-weight: 600;
  }
  .card--brand .holder__name .name-first { color: var(--brand-red); }
  .card--brand .holder__name .name-last { color: var(--shadow-black); }

  .mark-ring {
    position: absolute;
    left: 140px;
    top: 220px;
    width: 150px;
    height: 150px;
    border-radius: 50%;
    border: 12px solid var(--steel-grey);
  }
  .card--brand .wordmark {
    position: absolute;
    left: 318px;
    top: 272px;
    font-size: 36px;
  }
</style>
</head>
<body>
  <section class="card card--info">
    <div class="wordmark">Ridgeline Outfitters</div>
    <div class="holder holder__name"><span class="name-first">Milo</span> Brandt</div>
    <div class="holder holder__title">Owner</div>
    <div class="contact contact__phone">
      <svg width="22" height="26" viewBox="0 0 22 26" aria-hidden="true">
        <rect x="3" y="1" width="16" height="24" rx="3" fill="none" stroke="var(--shadow-black)" stroke-width="3"/>
        <rect x="8" y="20" width="6" height="2" fill="var(--shadow-black)"/>
      </svg>612-555-0187
    </div>
    <div class="contact contact__web">www.ridgelineoutfittersmn.example</div>
  </section>

  <section class="card card--brand">
    <div class="holder__name"><span class="name-first">Milo</span> <span class="name-last">Brandt</span></div>
    <div class="mark-ring"></div>
    <div class="wordmark">Ridgeline Outfitters</div>
  </section>
</body>
</html>
```